St Louis Electrician Needing a Business Card Design!!

We are a St Louis based electrical contracting firm that needs help designing a business card. We have a logo and I have another image that I would like to incorporate. Open to ideas..Thanks!!

Industry/Entity Type

Business

Requirements
Must have
• there are two downloads...one is the logo and the other is what i was wanting coming off the logo...the light rays. Like the logo with the blue background...Was thinking the whole card would be that color blue.
Should not have
• No lightning bolts

```html
<!DOCTYPE html>
<html lang="en">
<head>
<meta charset="utf-8">
<title>BrightVolt Inc. – Business Card</title>
<link href="https://fonts.googleapis.com/css2?family=Open+Sans:wght@400;600;700&display=swap" rel="stylesheet">
<style>
  :root {
    --stage: #e9e4dc;
    --brand-blue: #1f64b3;
    --card-white: #f7f7f7;
    --band-grey: #b3b6ba;
    --ink-grey: #9a9a9a;
  }
  * { box-sizing: border-box; margin: 0; padding: 0; }
  html, body { width: 1200px; height: 1022px; overflow: hidden; }
  body {
    background: var(--stage);
    font-family: "Open Sans", Arial, sans-serif;
    display: flex;
    flex-direction: column;
    align-items: center;
    justify-content: center;
    gap: 62px;
  }
  .card {
    position: relative;
    width: 700px;
    height: 400px;
    border-radius: 22px;
    overflow: hidden;
    box-shadow: 0 6px 18px rgba(0,0,0,0.18);
  }
  .card-art { position: absolute; inset: 0; width: 100%; height: 100%; }

  .company-name {
    position: absolute;
    left: 44px;
    bottom: 70px;
    color: #ffffff;
    font-weight: 400;
    font-size: 38px;
    letter-spacing: 0.5px;
    white-space: nowrap;
  }

  .contact {
    position: absolute;
    top: 96px;
    right: 44px;
    width: 270px;
    text-align: right;
    color: var(--brand-blue);
  }
  .contact-name { font-size: 28px; font-weight: 700; letter-spacing: 0.5px; line-height: 1; white-space: nowrap; }
  .contact-role { font-size: 14px; color: var(--ink-grey); letter-spacing: 1px; margin-top: 6px; }
  .contact-lines { margin-top: 22px; font-size: 17px; line-height: 1.45; }
  .contact-line { display: flex; align-items: center; justify-content: flex-end; gap: 10px; white-space: nowrap; }
  .contact-icon { width: 15px; height: 15px; flex: none; }
</style>
</head>
<body>

  <section class="card card-front">
    <svg class="card-art" viewBox="0 0 700 400" aria-hidden="true">
      <defs>
        <radialGradient id="blueGlowFront" cx="0.25" cy="0.65" r="0.7">
          <stop offset="0" stop-color="#4a92d4"/>
          <stop offset="1" stop-color="#1553a0"/>
        </radialGradient>
      </defs>
      <rect width="700" height="400" fill="url(#blueGlowFront)"/>
      <path d="M352,0 C342,150 322,280 312,400 L332,400 C342,280 362,150 372,0 Z" fill="var(--band-grey)"/>
      <path d="M372,0 L700,0 L700,400 L332,400 C342,280 362,150 372,0 Z" fill="var(--card-white)"/>
      <path d="M372,0 C362,150 342,280 332,400" fill="none" stroke="var(--brand-blue)" stroke-width="3"/>
      <rect x="664" y="48" width="36" height="22" fill="var(--brand-blue)"/>
    </svg>
    <div class="company-name">BrightVolt Inc.</div>
    <div class="contact">
      <div class="contact-name">MARK ELLISON</div>
      <div class="contact-role">OWNER</div>
      <div class="contact-lines">
        <div class="contact-line">+33 2000-1410
          <svg class="contact-icon" viewBox="0 0 16 16"><path d="M3 1h3l1 4-2 1c1 2 2 3 4 4l1-2 4 1v3c0 1-1 2-2 2C6 14 2 10 1 3c0-1 1-2 2-2z" fill="#9a9a9a"/></svg>
        </div>
        <div class="contact-line">+33 2000-1522
          <svg class="contact-icon" viewBox="0 0 16 16"><rect x="4" y="1" width="8" height="5" fill="#9a9a9a"/><rect x="1" y="6" width="14" height="6" rx="1" fill="#9a9a9a"/><rect x="4" y="10" width="8" height="5" fill="#ccc"/></svg>
        </div>
        <div class="contact-line">mark@brightvoltmail.com
          <svg class="contact-icon" viewBox="0 0 16 16"><rect x="1.5" y="3.5" width="13" height="9" fill="none" stroke="#9a9a9a" stroke-width="1.4"/><path d="M1.5 3.5 8 9l6.5-5.5" fill="none" stroke="#9a9a9a" stroke-width="1.4"/></svg>
        </div>
      </div>
    </div>
  </section>

  <section class="card card-second">
    <svg class="card-art" viewBox="0 0 700 400" aria-hidden="true">
      <defs>
        <radialGradient id="blueGlowSecond" cx="0.25" cy="0.6" r="0.7">
          <stop offset="0" stop-color="#3f86cc"/>
          <stop offset="1" stop-color="#1553a0"/>
        </radialGradient>
      </defs>
      <rect width="700" height="400" fill="url(#blueGlowSecond)"/>
      <path d="M352,0 C342,150 322,280 312,400 L332,400 C342,280 362,150 372,0 Z" fill="var(--band-grey)"/>
      <path d="M372,0 L700,0 L700,400 L332,400 C342,280 362,150 372,0 Z" fill="var(--card-white)"/>
      <path d="M372,0 C362,150 342,280 332,400" fill="none" stroke="var(--brand-blue)" stroke-width="3"/>
      <rect x="664" y="48" width="36" height="22" fill="var(--brand-blue)"/>
    </svg>
    <div class="contact">
      <div class="contact-name">MARK ELLISON</div>
      <div class="contact-role">OWNER</div>
      <div class="contact-lines">
        <div class="contact-line">+33 2000-1410
          <svg class="contact-icon" viewBox="0 0 16 16"><path d="M3 1h3l1 4-2 1c1 2 2 3 4 4l1-2 4 1v3c0 1-1 2-2 2C6 14 2 10 1 3c0-1 1-2 2-2z" fill="#9a9a9a"/></svg>
        </div>
        <div class="contact-line">+33 2000-1522
          <svg class="contact-icon" viewBox="0 0 16 16"><rect x="4" y="1" width="8" height="5" fill="#9a9a9a"/><rect x="1" y="6" width="14" height="6" rx="1" fill="#9a9a9a"/><rect x="4" y="10" width="8" height="5" fill="#ccc"/></svg>
        </div>
        <div class="contact-line">mark@brightvoltmail.com
          <svg class="contact-icon" viewBox="0 0 16 16"><rect x="1.5" y="3.5" width="13" height="9" fill="none" stroke="#9a9a9a" stroke-width="1.4"/><path d="M1.5 3.5 8 9l6.5-5.5" fill="none" stroke="#9a9a9a" stroke-width="1.4"/></svg>
        </div>
      </div>
    </div>
  </section>

</body>
</html>
```